Cybersecurity company is looking for business card.

I need a business card design for our company, we are a cybersecurity company providing advance technology to protect agains any kind of malware. We need a fresh modern design it should communicate modern, technology and growth.

Target Market(s)

Business to business

Industry/Entity Type

Business

Contact Information for Business Card

Should have location, address, fax, mobile, phone, email and website.

Requirements
Must have
• Must follow company's logo color and style. Must have the company's log on its.

```html
<!DOCTYPE html>
<html lang="en">
<head>
<meta charset="utf-8">
<title>Veltrix Business Card</title>
<link rel="stylesheet" href="https://fonts.googleapis.com/css2?family=Arimo:wght@400;700&display=swap">
<style>
  :root {
    --brand-red: #a31e22;
    --ink-black: #000000;
    --paper-white: #ffffff;
    --backdrop: #1e1e1e;
    --text-dark: #111111;
  }
  * { margin: 0; padding: 0; box-sizing: border-box; }
  html, body { width: 1200px; height: 800px; overflow: hidden; }
  body {
    background: var(--backdrop);
    font-family: "Arimo", Arial, sans-serif;
    position: relative;
  }
  .card {
    position: absolute;
    top: 263px;
    width: 479px;
    height: 274px;
    overflow: hidden;
  }
  .card-front { left: 100px; background: var(--ink-black); }
  .card-back { left: 623px; background: var(--paper-white); }
  .card-shape { position: absolute; inset: 0; width: 100%; height: 100%; }

  .wordmark {
    position: absolute;
    font-weight: 700;
    letter-spacing: 1px;
    line-height: 1;
  }
  .card-front .wordmark {
    right: 44px;
    top: 160px;
    font-size: 52px;
    color: var(--paper-white);
  }
  .front-web {
    position: absolute;
    left: 187px;
    top: 221px;
    font-size: 10px;
    letter-spacing: 6.2px;
    color: var(--brand-red);
  }
  .card-back .wordmark {
    left: 26px;
    top: 48px;
    font-size: 56px;
    color: var(--ink-black);
  }
  .address {
    position: absolute;
    left: 27px;
    top: 141px;
    font-size: 11.5px;
    line-height: 14px;
    color: var(--text-dark);
    font-style: normal;
  }
  .contact-list {
    position: absolute;
    left: 27px;
    top: 205px;
    list-style: none;
    font-size: 11.5px;
    line-height: 14px;
    color: var(--text-dark);
  }
  .contact-label {
    color: var(--brand-red);
    font-weight: 700;
    font-size: 9px;
  }
  .online {
    position: absolute;
    right: 26px;
    top: 205px;
    text-align: right;
    color: var(--paper-white);
  }
  .online-email { font-size: 13px; display: block; line-height: 16px; }
  .online-web { font-size: 21px; font-weight: 700; display: block; line-height: 26px; }
</style>
</head>
<body>
  <section class="card card-front" aria-label="Card front">
    <svg class="card-shape" viewBox="0 0 479 274" aria-hidden="true">
      <polygon points="0,0 308,0 50,274 0,274" fill="var(--brand-red)"/>
    </svg>
    <div class="wordmark">Veltrix</div>
    <div class="front-web">www.veltrix-secure.com</div>
  </section>

  <section class="card card-back" aria-label="Card back">
    <svg class="card-shape" viewBox="0 0 479 274" aria-hidden="true">
      <polygon points="447,0 479,0 479,274 172,274" fill="var(--brand-red)"/>
    </svg>
    <div class="wordmark">Veltrix</div>
    <address class="address">
      Dubai - UAE<br>
      Harbor Tech Park (HTP)<br>
      Marina Avenue.
    </address>
    <ul class="contact-list">
      <li><span class="contact-label">mobile</span> +971 50 555 XXXX</li>
      <li><span class="contact-label">phone</span> 04 555 XXXX</li>
      <li><span class="contact-label">fax</span> 04 555 XXXX</li>
    </ul>
    <div class="online">
      <span class="online-email">name.surname@veltrix-secure.com</span>
      <span class="online-web">www.veltrix-secure.com</span>
    </div>
  </section>
</body>
</html>
```